Investment Company Business Card Design

We need a Business Card design for a new company based in Boston called "Olt Investment". We are cooperating with local real estate and construction companies. Our company is very actively and aggressively acquiring primarily residential investment properties either to buy and hold long term or for purposes or renovating and repositioning for re-sale in the market. In addition, we undertake some development projects and acquisitions as opportunities present themselves. the final design should contains information about “Olt" the river boat. we are tenacious, indomitable, and the business have a favorable wind throughout the voyage for all our investment.
sample Info. on Design:
Tem Hollis
CEO
508-xxx-xxxx
415 Marrow St. Suite 108, Boston, MA 02127
Please provide a template also, that we can edit the info later.
Reason: i just got new LOGO Design attached will be use in Business Card Design.
Construction

```html
<!DOCTYPE html>
<html lang="en">
<head>
<meta charset="utf-8">
<title>Olt Investment — Business Card</title>
<link rel="stylesheet" href="https://fonts.googleapis.com/css2?family=Montserrat:wght@400;700&display=swap">
<style>
  :root {
    --page: #ffffff;
    --front-bg: #000000;
    --front-text: #ffffff;
    --gold: #c9a658;
    --band-dark: rgba(40, 40, 40, 0);
    --band-mid: rgba(60, 60, 60, 0.55);
    --back-bg: #86774f;
    --back-ink: #a7987a;
  }
  html, body {
    margin: 0;
    padding: 0;
    width: 1034px;
    height: 1200px;
    overflow: hidden;
    background: var(--page);
  }
  .canvas {
    position: relative;
    width: 1034px;
    height: 1200px;
  }
  .card {
    position: absolute;
    left: 113px;
    width: 810px;
    height: 450px;
    overflow: hidden;
  }
  .card--front {
    top: 102px;
    background: var(--front-bg);
    border-radius: 225px 0 0 225px;
    color: var(--front-text);
  }
  .card--back {
    top: 634px;
    height: 451px;
    background: var(--back-bg);
    border-radius: 0 226px 226px 0;
  }
  .decor-band {
    position: absolute;
    left: 0;
    top: 240px;
    width: 810px;
    height: 150px;
    background: linear-gradient(170deg, var(--band-dark) 20%, var(--band-mid) 50%, var(--band-dark) 80%);
  }
  .contact {
    position: absolute;
    left: 98px;
    top: 124px;
    font-family: "Montserrat", sans-serif;
    line-height: 1;
  }
  .contact__name {
    font-weight: 700;
    font-size: 23px;
    letter-spacing: 0.5px;
    margin: 0 0 9px;
  }
  .contact__role {
    font-size: 18px;
    margin: 0 0 9px;
  }
  .contact__phone {
    font-size: 22px;
    letter-spacing: 0.3px;
    margin: 0;
  }
  .brand-name {
    position: absolute;
    margin: 0;
    font-family: "Montserrat", sans-serif;
    font-weight: 400;
    line-height: 1;
    white-space: nowrap;
  }
  .brand-name--front {
    left: 410px;
    top: 172px;
    font-size: 30px;
    color: var(--gold);
  }
  .brand-name--back {
    left: 42px;
    top: 196px;
    font-size: 62px;
    color: var(--back-ink);
  }
  .address {
    position: absolute;
    left: 258px;
    top: 355px;
    display: flex;
    align-items: center;
    gap: 10px;
    font-family: "Montserrat", sans-serif;
    font-size: 18.5px;
    margin: 0;
    white-space: nowrap;
  }
  .address__icon {
    width: 14px;
    height: 19px;
    flex: none;
  }
</style>
</head>
<body>
<main class="canvas">

  <section class="card card--front" aria-label="Business card front">
    <div class="decor-band" role="img" aria-label="Soft grey decorative sweep across the card"></div>

    <div class="contact">
      <p class="contact__name">TEM HOLLIS</p>
      <p class="contact__role">CEO</p>
      <p class="contact__phone">508-xxx-xxxx</p>
    </div>

    <p class="brand-name brand-name--front">Olt Investment</p>

    <p class="address">
      <svg class="address__icon" viewBox="0 0 14 19" aria-hidden="true">
        <path d="M7 0 C3.1 0 0 3 0 6.8 C0 11.6 7 19 7 19 C7 19 14 11.6 14 6.8 C14 3 10.9 0 7 0 Z M7 9.4 A2.6 2.6 0 1 1 7 4.2 A2.6 2.6 0 1 1 7 9.4 Z" fill="var(--front-text)"/>
      </svg>
      <span>415 Marrow St. Suite 108, Boston, MA 02127</span>
    </p>
  </section>

  <section class="card card--back" aria-label="Business card back">
    <p class="brand-name brand-name--back">Olt Investment</p>
  </section>

</main>
</body>
</html>
```